6' Banner Stands for exhibiting to Health Fairs with an audience of age 55+

We need designs for two 6' banner stands to stand on either side of our exhibition tables. We offer Hereditary Cancer Screening. I want the banners to have the same look and feel as the logo and the files color scheme logo, etc..

The Banners should have "Hereditary Cancer Screening" at the top with the Tag Line "The Test You Take For Them" underneath. A photo of grandparents with kids/grandkids and underneath the photos in large font one of the following messages:
1) "A Simple Swab Could Save A Family Members LIFE Get Tested Today!"
2) "Does Cancer Run In Your Family? Get Tested Today!"
3) "Knowledge Is Power" "Get Tested Today!"
4) "Will You Give Your Loved Ones The Information To Beat Cancer In Their Lives? Get Tested Today!
5) Knowledge Is Power Get Tested Today!"
Updates

Thank you all for your designs I now have the exact specs for the banners, so please use these as you update your designs. 31.5 inches X 83.25 inches and add a 1/2 inch bleed to all 4 sides. Thank you.

Target Market(s)

Persons 55+ who are grandparents

Industry/Entity Type

Healthcare

Font styles to use
Sans Serif
Other font styles liked:
• Comic Sans for "The Test You Take For Them"

Colors
9bcb3c
0356a4
ffffff

Requirements
Must have
• the main focus should be the hereditary cancer screening; "Hereditary Cancer Screening";
• "The test you order for them" in Comic Sans font underneath
• A photo or photos of grandparents with their grandchildren (multiple ethnicities)
• One of the slogans listed above
• GET TESTED TODAY underneath the messages at the bottom of the banner highlighted and eye catching
• www.kinhealthcheckup.net
Nice to have
• Logo at the top or bottom

```html
<!DOCTYPE html>
<html lang="en">
<head>
<meta charset="utf-8">
<title>Hereditary Cancer Screening – Banner Stands</title>
<link rel="stylesheet" href="https://fonts.googleapis.com/css2?family=Bebas+Neue&family=Comic+Neue:wght@700&family=Roboto+Condensed:wght@800&family=Montserrat:wght@500;700;800&display=swap">
<style>
  :root {
    --navy: #161b4c;
    --title-navy: #1b2158;
    --green: #8cc63f;
    --green-text: #5f9e22;
    --white: #ffffff;
    --stage: #e4e4e7;
    --caption: #333338;
    --photo-warm: #d9c2a8;
    --photo-sky: #b9d7e6;
    --photo-garden: #8fae6a;
  }
  * { box-sizing: border-box; margin: 0; padding: 0; }
  html, body { width: 1200px; height: 963px; overflow: hidden; }
  body { background: var(--stage); position: relative; font-family: "Montserrat", sans-serif; }

  .banner {
    position: absolute; top: 78px; width: 300px; height: 705px;
    background: var(--white); overflow: hidden;
  }
  .banner--one { left: 62px; }
  .banner--two { left: 446px; }
  .banner--three { left: 830px; }

  .banner__title {
    position: absolute; top: 22px; left: -50px; width: 400px;
    font-family: "Bebas Neue", sans-serif; font-weight: 400; color: var(--title-navy);
    text-align: center; line-height: 50px; font-size: 56px;
    white-space: nowrap;
    transform: scaleX(0.78); transform-origin: center top;
  }
  .banner__tagline {
    position: absolute; top: 134px; left: 0; width: 100%;
    font-family: "Comic Neue", sans-serif; font-weight: 700; font-size: 17px;
    color: var(--green-text); text-align: center; white-space: nowrap;
  }

  .banner__photo { position: absolute; left: 0; width: 100%; }
  .banner--one .banner__photo { top: 180px; height: 260px; background: linear-gradient(160deg, #efe6dc, var(--photo-warm) 60%, #7c8fa8); }
  .banner--two .banner__photo { top: 163px; height: 240px; background: linear-gradient(180deg, #f2f7fa, var(--photo-sky) 45%, #e6dccb); }
  .banner--three .banner__photo { top: 163px; height: 240px; background: linear-gradient(180deg, #c7b8a4, var(--photo-garden) 40%, #d8c5bd); }

  .banner__shapes { position: absolute; inset: 0; width: 300px; height: 705px; }

  .banner__inset {
    position: absolute; width: 72px; height: 72px; border-radius: 50%;
    border: 4px solid var(--green);
  }
  .inset--beach { left: 10px; top: 362px; background: linear-gradient(180deg, #bcd9ea, #e3d7c2); }
  .inset--hug { left: 98px; top: 350px; background: linear-gradient(180deg, #ddd1c4, #c9a891); }
  .inset--field { left: 204px; top: 345px; background: linear-gradient(180deg, #a9c28a, #6f9a4c); }

  .banner__headline {
    position: absolute; left: 0; width: 100%;
    font-family: "Roboto Condensed", sans-serif; font-weight: 800;
    color: var(--white); text-align: center; text-transform: uppercase;
    letter-spacing: -0.5px; white-space: nowrap;
  }
  .banner--one .banner__headline { top: 458px; font-size: 46px; line-height: 48px; }
  .banner--two .banner__headline { top: 420px; font-size: 43px; line-height: 46px; }
  .banner--three .banner__headline { top: 420px; font-size: 41px; line-height: 43px; }

  .banner__cta {
    position: absolute; left: 22px; width: 258px; height: 37px;
    background: var(--green); border-radius: 3px;
    color: var(--white); font-family: "Montserrat", sans-serif; font-weight: 800;
    font-size: 20px; line-height: 37px; text-align: center; text-transform: uppercase;
    white-space: nowrap;
  }
  .banner--one .banner__cta { top: 618px; }
  .banner--two .banner__cta, .banner--three .banner__cta { top: 608px; }

  .banner__url {
    position: absolute; left: 0; width: 100%;
    font-family: "Montserrat", sans-serif; font-weight: 700; font-size: 13px;
    color: var(--green); text-align: center; white-space: nowrap;
  }
  .banner--one .banner__url { top: 670px; }
  .banner--two .banner__url, .banner--three .banner__url { top: 662px; }

  .caption {
    position: absolute; top: 833px; width: 300px; text-align: center;
    font-weight: 500; font-size: 19px; color: var(--caption);
  }
  .caption--one { left: 62px; }
  .caption--two { left: 446px; }
  .caption--three { left: 830px; }

  .footnote {
    position: absolute; top: 905px; left: 0; width: 100%; text-align: center;
    font-weight: 500; font-size: 23px; color: var(--caption);
  }
</style>
</head>
<body>

  <section class="banner banner--one">
    <div class="banner__photo" role="img" aria-label="Photo of laughing grandparents playing with their grandchildren"></div>
    <svg class="banner__shapes" viewBox="0 0 300 705" aria-hidden="true">
      <path d="M0 190 Q60 160 150 170 Q230 178 300 150 L300 0 L0 0 Z" fill="var(--white)"/>
      <path d="M0 196 Q60 166 150 176 Q230 184 300 156 L300 148 Q230 172 150 162 Q60 152 0 178 Z" fill="var(--green)"/>
      <path d="M0 412 Q150 380 300 400 L300 705 L0 705 Z" fill="var(--green)"/>
      <path d="M0 420 Q150 390 300 408 L300 705 L0 705 Z" fill="var(--navy)"/>
    </svg>
    <div class="banner__inset inset--beach" role="img" aria-label="Family walking on a beach"></div>
    <div class="banner__inset inset--hug" role="img" aria-label="Grandfather hugging a grandchild"></div>
    <div class="banner__inset inset--field" role="img" aria-label="Family running across a field"></div>
    <h1 class="banner__title">Hereditary<br>Cancer Screening</h1>
    <p class="banner__tagline">"The Test You Take For Them"</p>
    <h2 class="banner__headline">Give Them<br>The Gift Of<br>Knowledge</h2>
    <div class="banner__cta">Get Tested Today</div>
    <p class="banner__url">www.kinhealthcheckup.net</p>
  </section>

  <section class="banner banner--two">
    <div class="banner__photo" role="img" aria-label="Photo of grandparents and grandchildren playing on a beach"></div>
    <svg class="banner__shapes" viewBox="0 0 300 705" aria-hidden="true">
      <path d="M0 372 Q150 408 300 362 L300 705 L0 705 Z" fill="var(--green)"/>
      <path d="M0 384 Q150 418 300 374 L300 705 L0 705 Z" fill="var(--navy)"/>
    </svg>
    <h1 class="banner__title">Hereditary<br>Cancer Screening</h1>
    <p class="banner__tagline">"The Test You Take For Them"</p>
    <h2 class="banner__headline">Does<br>Cancer Run<br>In Your<br>Family</h2>
    <div class="banner__cta">Get Tested Today</div>
    <p class="banner__url">www.kinhealthcheckup.net</p>
  </section>

  <section class="banner banner--three">
    <div class="banner__photo" role="img" aria-label="Photo of grandparents sitting with grandchildren in a garden"></div>
    <svg class="banner__shapes" viewBox="0 0 300 705" aria-hidden="true">
      <path d="M0 372 Q150 408 300 362 L300 705 L0 705 Z" fill="var(--green)"/>
      <path d="M0 384 Q150 418 300 374 L300 705 L0 705 Z" fill="var(--navy)"/>
    </svg>
    <h1 class="banner__title">Hereditary<br>Cancer Screening</h1>
    <p class="banner__tagline">"The Test You Take For Them"</p>
    <h2 class="banner__headline">A Simple<br>Swab Could<br>Save A Family<br>Members Life</h2>
    <div class="banner__cta">Get Tested Today</div>
    <p class="banner__url">www.kinhealthcheckup.net</p>
  </section>

  <p class="caption caption--one">STANDEE 1</p>
  <p class="caption caption--two">STANDEE 2</p>
  <p class="caption caption--three">STANDEE 3</p>

  <p class="footnote">6' BANNER STANDS FOR EXHIBITING TO HEALTH FAIRS WITH AN AUDIENCE OF AGE 55+</p>

</body>
</html>
```